ORV NETWORKS LTD

going to a headteacher conference need a sign to show our services:
www.orv-networks.co.uk
will attach a leaflet showing some more information.

Services:
IT Support
Web Design
Data Cabling (Fibre/Cat6)
Broadband
Hardware sales
WIFI
CCTV
Audio Visual
Door Access System
VOIP Telephone

```html
<!DOCTYPE html>
<html lang="en">
<head>
<meta charset="utf-8">
<title>ORV Networks – Services Banner</title>
<link href="https://fonts.googleapis.com/css2?family=Poppins:wght@500;600;700&display=swap" rel="stylesheet">
<style>
  :root{
    --page:#b3b3b3;
    --white:#ffffff;
    --blue:#0a6dbb;
    --blue-deep:#0c5ea6;
    --orange:#f07c45;
    --ink:#1b1b1b;
    --dark:#202020;
  }
  *{margin:0;padding:0;box-sizing:border-box}
  html,body{width:1200px;height:1200px;overflow:hidden;background:var(--page);font-family:"Poppins",sans-serif}
  .banner{position:absolute;left:358px;top:53px;width:435px;height:1093px;background:var(--white);overflow:hidden}
  .banner-shapes{position:absolute;left:0;top:0}
  .brand{position:absolute;top:44px;left:0;width:100%;display:flex;justify-content:center;align-items:center;gap:8px}
  .brand-mark{width:16px;height:16px;background:var(--blue);border-radius:3px}
  .brand-name{font-weight:700;font-size:20px;color:var(--blue);letter-spacing:.5px;line-height:1}
  .tagline{position:absolute;top:85px;width:100%;text-align:center;font-size:8.5px;font-weight:500;color:var(--blue);letter-spacing:.6px}
  .headline{position:absolute;top:110px;width:100%;text-align:center;font-weight:700;line-height:39px;font-size:43px;letter-spacing:-.5px}
  .headline .blue{color:var(--blue)}
  .headline .orange{color:var(--orange);font-size:44px}
  .headline .amp{font-weight:500}
  .sub-of{position:absolute;top:234px;width:100%;text-align:center;font-weight:700;font-size:29px;color:var(--ink);line-height:34px}
  .sub-of::before,.sub-of::after{content:"";position:absolute;top:18px;height:1.5px;background:var(--ink);width:112px}
  .sub-of::before{left:61px}.sub-of::after{right:61px}
  .sub-tech{position:absolute;top:264px;width:100%;text-align:center;font-weight:700;font-size:30px;color:var(--ink);line-height:36px}
  .services-title{position:absolute;top:594px;width:100%;text-align:center;color:var(--white);font-weight:700;font-size:25px;letter-spacing:.3px}
  .service{position:absolute;display:flex;align-items:center;color:var(--white);font-weight:700;font-size:15px;line-height:18px}
  .service .icon{width:32px;height:32px;border-radius:50%;background:var(--orange);flex:none;margin-right:17px;display:flex;align-items:center;justify-content:center}
  .phone{position:absolute;left:55px;top:970px;width:323px;height:48px;border-radius:24px;background:var(--orange);display:flex;align-items:center;justify-content:center;gap:10px;color:var(--white);font-weight:700;font-size:36px;letter-spacing:-.5px}
  .web{position:absolute;top:1030px;width:100%;text-align:center;color:var(--white);font-weight:500;font-size:28px;letter-spacing:-.3px}
  .web .domain{color:var(--blue);font-weight:600}
</style>
</head>
<body>
<div class="banner">
  <svg class="banner-shapes" width="435" height="1093" viewBox="0 0 435 1093">
    <defs>
      <linearGradient id="photoTone" x1="0" y1="0" x2="1" y2="1">
        <stop offset="0" stop-color="#c9b7a4"/>
        <stop offset=".5" stop-color="#9b8d80"/>
        <stop offset="1" stop-color="#6f6b6a"/>
      </linearGradient>
    </defs>
    <rect x="0" y="290" width="435" height="310" fill="url(#photoTone)" role="img" aria-label="Photo of children working with laptops and robotics kits in a classroom"/>
    <path d="M0 290 H55 Q218 380 382 290 H435 V0 H0 Z" fill="var(--white)"/>
    <path d="M0 582 H55 Q218 520 382 582 H435 V1093 H0 Z" fill="var(--orange)"/>
    <path d="M0 588 H55 Q218 530 382 588 H435 V1093 H0 Z" fill="var(--blue)"/>
    <rect x="0" y="998" width="435" height="95" fill="var(--dark)"/>
  </svg>

  <div class="brand"><span class="brand-mark"></span><span class="brand-name">ORV NETWORKS LTD</span></div>
  <div class="tagline">EDUCATION SUPPORT &amp; INSTALLATION</div>

  <h1 class="headline">
    <span class="blue">EDUCATION,</span><br>
    <span class="blue">SUPPORT <span class="amp">&amp;</span></span><br>
    <span class="orange">INSTALLATION</span>
  </h1>
  <div class="sub-of">of All</div>
  <div class="sub-tech">Technologies</div>

  <h2 class="services-title">OUR SERVICES</h2>

  <div class="service" style="left:64px;top:639px"><span class="icon"><svg width="16" height="16" viewBox="0 0 16 16" fill="none" stroke="#fff" stroke-width="1.4"><circle cx="8" cy="8" r="3"/><path d="M8 1v3M8 12v3M1 8h3M12 8h3"/></svg></span>IT Support</div>
  <div class="service" style="left:64px;top:700px"><span class="icon"><svg width="16" height="16" viewBox="0 0 16 16" fill="none" stroke="#fff" stroke-width="1.4"><rect x="2" y="3" width="12" height="8" rx="1"/><path d="M6 14h4M8 11v3"/></svg></span>Web Design</div>
  <div class="service" style="left:64px;top:770px"><span class="icon"><svg width="16" height="16" viewBox="0 0 16 16" fill="none" stroke="#fff" stroke-width="1.4"><path d="M2 4h8l4 2M2 8h12M2 12h8l4-2"/></svg></span>Data Cabling<br>(Fibre/Cat6)</div>
  <div class="service" style="left:64px;top:839px"><span class="icon"><svg width="16" height="16" viewBox="0 0 16 16" fill="none" stroke="#fff" stroke-width="1.4"><rect x="2" y="10" width="12" height="4" rx="1"/><path d="M11 10V3M4 7a4 4 0 0 1 4-2"/></svg></span>Broadband</div>
  <div class="service" style="left:64px;top:908px"><span class="icon"><svg width="16" height="16" viewBox="0 0 16 16" fill="none" stroke="#fff" stroke-width="1.4"><rect x="4" y="2" width="8" height="12" rx="4"/><path d="M8 2v5"/></svg></span>Hardware<br>sales</div>

  <div class="service" style="left:237px;top:639px"><span class="icon"><svg width="16" height="16" viewBox="0 0 16 16" fill="none" stroke="#fff" stroke-width="1.4"><path d="M3 6a7 7 0 0 1 10 0M5 8.5a4 4 0 0 1 6 0"/><rect x="2" y="11" width="12" height="3" rx="1"/></svg></span>WIFI</div>
  <div class="service" style="left:237px;top:700px"><span class="icon"><svg width="16" height="16" viewBox="0 0 16 16" fill="none" stroke="#fff" stroke-width="1.4"><path d="M2 4l9 2-1 4-8-2zM10 9l1 4h3"/></svg></span>CCTV</div>
  <div class="service" style="left:237px;top:770px"><span class="icon"><svg width="16" height="16" viewBox="0 0 16 16" fill="none" stroke="#fff" stroke-width="1.4"><circle cx="8" cy="7" r="5"/><path d="M8 5v6"/></svg></span>Door Access<br>System</div>
  <div class="service" style="left:237px;top:839px"><span class="icon"><svg width="16" height="16" viewBox="0 0 16 16" fill="none" stroke="#fff" stroke-width="1.4"><rect x="2" y="2" width="9" height="9" rx="1"/><rect x="9" y="8" width="3" height="5" rx="1.5"/><path d="M10.5 13v2"/></svg></span>Audio Visual</div>
  <div class="service" style="left:237px;top:908px"><span class="icon"><svg width="16" height="16" viewBox="0 0 16 16" fill="none" stroke="#fff" stroke-width="1.4"><path d="M3 3l3 1-1 3a8 8 0 0 0 4 4l3-1 1 3-2 1C6 13 3 9 2 5z"/><circle cx="12" cy="4" r="2.5"/></svg></span>VOIP<br>Telephone</div>

  <div class="phone">
    <svg width="28" height="28" viewBox="0 0 24 24" fill="#fff"><path d="M6.6 10.8a15 15 0 0 0 6.6 6.6l2.2-2.2c.3-.3.7-.4 1-.2 1.1.4 2.3.6 3.6.6.6 0 1 .4 1 1V20c0 .6-.4 1-1 1A17 17 0 0 1 3 4c0-.6.4-1 1-1h3.5c.6 0 1 .4 1 1 0 1.3.2 2.5.6 3.6.1.3 0 .7-.2 1z"/></svg>
    <span>0161 555 0142</span>
  </div>
  <div class="web">www.<span class="domain">orv-networks</span>.co.uk</div>
</div>
</body>
</html>
```